Mural for a photo shoot area in an ice cream store

This mural project is for an interactive photo area for consumers in a shaved ice store. We are looking for a design that goes around the 3 sides of wall and with the main theme in the center wall where the logo and feature element will be. Already have company logo and feature product element and need to incorporate them into the mural design. The company name in Hokkien language means flipping table which is incorporated in the company logo.

Looking for a fun or cool design that consumers can interact with via their camera. The “table/logo” want to make with an actual table sticking out of the wall. The dimension of the walls is in the wall dimension in mm.pdf and unit is in mm.

Target Market(s)

The intended product audience is 16-35 years of age consumers.

Industry/Entity Type

Food Store

Requirements
Must have
• Incorporate the company logo and featured character provided.
Nice to have
• cool or bold factor that will make IG more interesting or talk about.

```html
<!DOCTYPE html>
<html lang="en">
<head>
<meta charset="utf-8">
<title>Tilt Table – Photo Wall Mural</title>
<link rel="stylesheet" href="https://fonts.googleapis.com/css2?family=Quicksand:wght@600&display=swap">
<style>
  :root {
    --paper: #ffffff;
    --sunshine: #ffe100;
    --stripe-deep: #f0c020;
    --stripe-mid: #fcd94a;
    --stripe-light: #fff08c;
    --chevron-1: #fff6b0;
    --chevron-2: #ffee88;
    --chevron-3: #ffd35a;
    --chevron-4: #fcd23a;
    --feature-orange: #eb5324;
    --ink: #231815;
    --sun-line: rgba(255, 255, 255, 0.75);
    --fruit-line: rgba(255, 246, 176, 0.8);
  }
  * { margin: 0; padding: 0; box-sizing: border-box; }
  html, body { width: 1200px; height: 1200px; overflow: hidden; background: var(--paper); }
  .mural { position: relative; width: 1200px; height: 1200px; background: var(--paper); }

  .side-wall { position: absolute; }
  .side-wall--left {
    left: 51px; top: 100px; width: 168px; height: 988px;
    background: repeating-linear-gradient(172deg,
      var(--stripe-deep) 0 28px, var(--paper) 28px 46px,
      var(--stripe-mid) 46px 74px, var(--paper) 74px 92px,
      var(--stripe-light) 92px 120px, var(--paper) 120px 140px);
  }
  .side-wall--right {
    left: 858px; top: 94px; width: 288px; height: 990px;
    background: repeating-linear-gradient(168deg,
      var(--stripe-deep) 0 28px, var(--paper) 28px 46px,
      var(--stripe-mid) 46px 74px, var(--paper) 74px 92px,
      var(--stripe-light) 92px 120px, var(--paper) 120px 140px);
  }

  .center-wall { position: absolute; left: 231px; top: 78px; width: 618px; height: 1008px; background: var(--sunshine); overflow: hidden; }
  .center-wall__bands { position: absolute; inset: 0; }

  .feature-panel { position: absolute; left: 155px; top: 606px; width: 306px; height: 402px; background: var(--feature-orange); }

  .artwork { position: absolute; }
  .artwork--sun {
    left: 11px; top: 2px; width: 376px; height: 376px; border-radius: 50%;
    background: radial-gradient(circle,
      rgba(255,255,255,0.18) 0 42%, var(--sun-line) 43% 45%,
      rgba(255,255,255,0.32) 46% 100%);
  }
  .artwork--lemon {
    left: 317px; top: 320px; width: 292px; height: 292px; border-radius: 50%;
    background: radial-gradient(circle,
      rgba(255,246,176,0.35) 0 82%, var(--fruit-line) 83% 86%,
      rgba(255,246,176,0.2) 87% 97%, var(--fruit-line) 98% 100%);
  }
  .artwork--strawberry {
    left: 0; top: 556px; width: 210px; height: 242px; border-radius: 48% 48% 52% 52% / 40% 40% 60% 60%;
    background: linear-gradient(180deg, rgba(255,246,176,0.45), rgba(255,246,176,0.3));
  }
  .artwork--cat-left {
    left: 60px; top: 716px; width: 152px; height: 132px; border-radius: 12px;
    background: linear-gradient(180deg, #fffaf0, #fcd25a);
  }
  .artwork--cat-right {
    left: 868px; top: 576px; width: 288px; height: 190px; border-radius: 16px;
    background: linear-gradient(180deg, #fffaf0, #fcd25a);
  }

  .brand { position: absolute; left: 462px; top: 822px; width: 200px; display: flex; align-items: center; gap: 10px; }
  .brand__dot { width: 22px; height: 22px; border-radius: 50%; border: 2px solid var(--ink); flex: none; }
  .brand__name { font-family: "Quicksand", sans-serif; font-weight: 600; font-size: 34px; color: var(--ink); white-space: nowrap; }
</style>
</head>
<body>
<main class="mural">
  <section class="side-wall side-wall--left"></section>
  <section class="side-wall side-wall--right"></section>

  <section class="center-wall">
    <div class="feature-panel"></div>
    <svg class="center-wall__bands" width="618" height="1008" viewBox="0 0 618 1008">
      <polygon fill="var(--chevron-1)" points="365,0 415,250 618,262 618,0"/>
      <polygon fill="var(--chevron-2)" points="433,0 473,194 618,202 618,0"/>
      <polygon fill="var(--chevron-3)" points="497,0 525,139 618,142 618,0"/>
      <polygon fill="var(--chevron-4)" points="533,0 557,98 618,102 618,0"/>
      <polygon fill="var(--chevron-1)" fill-opacity="0.8" points="0,766 213,777 261,1008 0,1008"/>
      <polygon fill="var(--chevron-2)" fill-opacity="0.8" points="0,806 189,817 231,1008 0,1008"/>
      <polygon fill="var(--chevron-3)" fill-opacity="0.8" points="0,866 133,870 161,1008 0,1008"/>
    </svg>
    <div class="artwork artwork--sun" role="img" aria-label="White line drawing of a smiling sun with long rays"></div>
    <div class="artwork artwork--lemon" role="img" aria-label="Pale line drawing of a lemon slice"></div>
    <div class="artwork artwork--strawberry" role="img" aria-label="Pale line drawing of a strawberry with leaves"></div>
  </section>

  <div class="artwork artwork--cat-left" role="img" aria-label="Mascot character sitting beside a small table with fruit and a drink"></div>
  <div class="artwork artwork--cat-right" role="img" aria-label="Mascot character flipping a small table with fruit and a drink"></div>

  <div class="brand">
    <span class="brand__dot"></span>
    <span class="brand__name">Tilt Table</span>
  </div>
</main>
</body>
</html>
```